American cannabis tech company business card design

Thrum.com is seeking a modern, professional, and brand-aligned business card that represents our company and its core values: Mission, Story, Values, and Impact. As an innovative cannabis company, we want a business card that is not only visually appealing but also serves as a representation of who we are and what we stand for.

Project Scope: Design a double-sided business card that integrates our brand identity and core values. Incorporate our key brand elements, ensuring a sleek and contemporary aesthetic. Visually reflect our core values (Mission, Story, Values, Impact) in a way that is engaging yet professional.

Target Market(s)

Vendors, third parties,

Contact Information for Business Card

Contact details (name, title, email, phone, website, etc.)

Font styles to use
Other font styles liked:
• Caslon, Centra

Colors

Designer to choose colors to be used in the design.

Requirements
Must have
• Thrum.com logo and branding A creative yet clean way to integrate our core values (Mission, Story, Values, Impact) Modern typography and a well-structured layout
Nice to have
• forest green, grey, white, black
Should not have
• references to marijuana, leafs, plants, or related product

```html
<!DOCTYPE html>
<html lang="en">
<head>
<meta charset="UTF-8">
<title>Thrum.com Business Card</title>
<link href="https://fonts.googleapis.com/css2?family=Montserrat:wght@400;500;600;800&display=swap" rel="stylesheet">
<style>
  :root {
    --forest: #183319;
    --forest-deep: #14301d;
    --leaf: #2a9430;
    --ink: #0f2b2b;
    --paper: #ffffff;
    --backdrop: #3a3b3d;
  }
  * { box-sizing: border-box; margin: 0; padding: 0; }
  html, body {
    width: 1200px; height: 1200px; overflow: hidden;
    background: var(--backdrop);
    font-family: "Montserrat", sans-serif;
  }
  .sheet {
    width: 1200px; height: 1200px;
    display: flex; flex-direction: column; align-items: center; justify-content: center;
    gap: 60px;
  }
  .card {
    position: relative;
    width: 900px; height: 514px;
    border-radius: 44px;
    overflow: hidden;
  }
  .card--front { background: var(--paper); }
  .card--back {
    background: var(--forest);
    box-shadow: inset 0 0 0 4px var(--leaf);
    display: flex; align-items: center; justify-content: center;
  }
  .wordmark {
    font-family: "Montserrat", sans-serif;
    font-weight: 800;
    letter-spacing: 2px;
    line-height: 1;
  }
  .card--front .wordmark {
    position: absolute; left: 520px; top: 120px;
    font-size: 86px; color: var(--forest);
  }
  .card--back .wordmark { font-size: 150px; color: var(--paper); }
  .identity { position: absolute; left: 70px; top: 245px; color: var(--ink); }
  .identity__name { font-size: 46px; font-weight: 600; letter-spacing: 1px; line-height: 1; }
  .identity__title { font-size: 24px; font-weight: 400; margin-top: 6px; letter-spacing: 1px; }
  .contacts { list-style: none; margin-top: 18px; }
  .contacts li {
    display: flex; align-items: center; gap: 14px;
    font-size: 26px; font-weight: 400; color: var(--ink); line-height: 40px;
  }
  .contacts svg { width: 26px; height: 26px; flex: none; }
  .stripe { position: absolute; left: 0; bottom: 0; width: 900px; height: 120px; }
</style>
</head>
<body>
<main class="sheet">
  <section class="card card--front" aria-label="Business card front">
    <div class="wordmark">THRUM</div>
    <div class="identity">
      <div class="identity__name">FULL NAME</div>
      <div class="identity__title">TITLE</div>
      <ul class="contacts">
        <li>
          <svg viewBox="0 0 24 24" aria-hidden="true"><path fill="#183319" d="M6.6 10.8c1.4 2.8 3.8 5.2 6.6 6.6l2.2-2.2c.3-.3.7-.4 1-.2 1.1.4 2.3.6 3.6.6.6 0 1 .4 1 1V20c0 .6-.4 1-1 1C10.6 21 3 13.4 3 4c0-.6.4-1 1-1h3.5c.6 0 1 .4 1 1 0 1.3.2 2.5.6 3.6.1.3 0 .7-.2 1z"/></svg>
          (000) 000 0000
        </li>
        <li>
          <svg viewBox="0 0 24 24" aria-hidden="true"><rect x="2" y="5" width="20" height="14" fill="#183319"/><path d="M2 5l10 8 10-8" fill="none" stroke="#fff" stroke-width="1.6"/></svg>
          email@company.com
        </li>
        <li>
          <svg viewBox="0 0 24 24" aria-hidden="true"><circle cx="12" cy="12" r="10" fill="none" stroke="#183319" stroke-width="2"/><ellipse cx="12" cy="12" rx="4.5" ry="10" fill="none" stroke="#183319" stroke-width="1.6"/><path d="M2 12h20M4 7h16M4 17h16" stroke="#183319" stroke-width="1.4"/></svg>
          www.company.com
        </li>
      </ul>
    </div>
    <svg class="stripe" viewBox="0 0 900 120" aria-hidden="true">
      <polygon points="0,96 640,96 628,120 0,120" fill="var(--forest)"/>
      <polygon points="660,58 900,58 900,120 636,120" fill="var(--leaf)"/>
      <rect x="0" y="114" width="900" height="6" fill="var(--leaf)"/>
    </svg>
  </section>
  <section class="card card--back" aria-label="Business card back">
    <div class="wordmark">THRUM</div>
  </section>
</main>
</body>
</html>
```